Business Card Design

We are a new residential construction company.our team is made up of young highly skilled tradesman of the next generation of carpenters coming through with new skills and ideas.we chose the name meridian as it means strikingly different from the rest as this is what we plan to be and we would like to portray this in our business card.we like Bold lettering as we want to make a statement, also the use of colour would be great as we want to stand out from the usual plain construction cards and logos.
I have attached a logo sketch I did as a rough idea if you can tidy it up or improve on it would be good.
I have also attached the LBP logo please include this on the card small but still legible.
open to any colourschemes ideas.
thanks
(note)please delete the LBP#804317 off from the card details please.
Industry/Entity Type
Construction
Contact Information for Business Card
MERIDIAN CONSTRUCTION LIMITED
Director:Tom Halvick
Mobile :0217364820
Email:Meridian.Construction@quillpost.example
Address:48 Wendle place,Ashgrove park 2091,Auckland
LBP#BP804317

```html
<!DOCTYPE html>
<html lang="en">
<head>
<meta charset="utf-8">
<title>Meridian Construction – Business Card</title>
<link href="https://fonts.googleapis.com/css2?family=Arimo:wght@400;700&display=swap" rel="stylesheet">
<style>
  :root {
    --page-bg: #eef0f4;
    --blueprint-deep: #1b2f9a;
    --blueprint-mid: #2f4fc4;
    --blueprint-light: #6f8ee6;
    --band-fill: rgba(196, 198, 244, 0.86);
    --band-line: #ffffff;
    --ink-navy: #1c2568;
    --brand-white: #ffffff;
  }
  * { box-sizing: border-box; margin: 0; padding: 0; }
  html, body {
    width: 1200px;
    height: 900px;
    overflow: hidden;
    background: var(--page-bg);
    font-family: "Arimo", Arial, sans-serif;
  }
  .business-card {
    position: absolute;
    left: 100px;
    top: 145px;
    width: 1000px;
    height: 610px;
    border-radius: 44px;
    overflow: hidden;
    box-shadow: 0 18px 40px rgba(20, 30, 80, 0.18);
  }
  .blueprint-backdrop {
    position: absolute;
    inset: 0;
    background:
      radial-gradient(ellipse at 70% 35%, var(--blueprint-light) 0%, rgba(111,142,230,0) 55%),
      linear-gradient(135deg, var(--blueprint-deep) 0%, var(--blueprint-mid) 55%, var(--blueprint-deep) 100%);
  }
  .brand-name {
    position: absolute;
    left: 0;
    right: 0;
    top: 95px;
    text-align: center;
    color: var(--brand-white);
    font-weight: 700;
    line-height: 1;
    text-transform: uppercase;
  }
  .brand-name .brand-primary {
    display: block;
    font-size: 112px;
    letter-spacing: 4px;
  }
  .brand-name .brand-secondary {
    display: block;
    margin-top: 14px;
    font-size: 78px;
    letter-spacing: 3px;
  }
  .contact-band {
    position: absolute;
    left: 0;
    right: 0;
    top: 370px;
    height: 170px;
    background: var(--band-fill);
    border-top: 3px solid var(--band-line);
    border-bottom: 3px solid var(--band-line);
    color: var(--ink-navy);
  }
  .holder {
    position: absolute;
    left: 70px;
    top: 26px;
    width: 300px;
  }
  .holder-name {
    font-size: 40px;
    font-weight: 700;
  }
  .holder-role {
    margin-top: 10px;
    margin-left: 148px;
    font-size: 28px;
  }
  .band-divider {
    position: absolute;
    left: 385px;
    top: 10px;
    bottom: 10px;
    width: 2px;
    background: var(--ink-navy);
    opacity: 0.55;
  }
  .contact-list {
    position: absolute;
    left: 402px;
    top: 12px;
    list-style: none;
    font-size: 27px;
    line-height: 36px;
  }
  .contact-list li {
    display: flex;
    align-items: flex-start;
  }
  .contact-icon {
    flex: 0 0 30px;
    width: 30px;
    height: 30px;
    margin: 3px 10px 0 0;
    fill: var(--ink-navy);
  }
  .address-lines { display: block; }
</style>
</head>
<body>
  <section class="business-card">
    <div class="blueprint-backdrop" role="img" aria-label="Blue architectural blueprint drawing filling the card background"></div>

    <h1 class="brand-name">
      <span class="brand-primary">Meridian</span>
      <span class="brand-secondary">Construction</span>
    </h1>

    <div class="contact-band">
      <div class="holder">
        <p class="holder-name">Tom Halvick</p>
        <p class="holder-role">Director</p>
      </div>
      <div class="band-divider"></div>
      <ul class="contact-list">
        <li>
          <svg class="contact-icon" viewBox="0 0 24 24" aria-hidden="true"><path d="M6.6 10.8a15.1 15.1 0 0 0 6.6 6.6l2.2-2.2a1 1 0 0 1 1-.25 11.4 11.4 0 0 0 3.6.57 1 1 0 0 1 1 1V20a1 1 0 0 1-1 1A17 17 0 0 1 3 4a1 1 0 0 1 1-1h3.5a1 1 0 0 1 1 1c0 1.25.2 2.45.57 3.57a1 1 0 0 1-.25 1z"/></svg>
          <span>0217364820</span>
        </li>
        <li>
          <svg class="contact-icon" viewBox="0 0 24 24" aria-hidden="true"><path d="M2 6.5 12 13l10-6.5V19a1 1 0 0 1-1 1H3a1 1 0 0 1-1-1z"/><path d="M3 4h18a1 1 0 0 1 .9.6L12 11 2.1 4.6A1 1 0 0 1 3 4z"/></svg>
          <span>Meridian.Construction@quillpost.example</span>
        </li>
        <li>
          <svg class="contact-icon" viewBox="0 0 24 24" aria-hidden="true"><path d="M12 3 2 12h3v9h5v-6h4v6h5v-9h3z"/></svg>
          <span class="address-lines">48 Wendle place,Ashgrove park<br>2091,Auckland</span>
        </li>
      </ul>
    </div>
  </section>
</body>
</html>
```